"Under Brambled Skies" cat novel book cover

Cover for a novel about a vet tech who saves two kittens from euthanization and ends up entangled in an adventure she never could have dreamed.

Novel has four point-of-view characters: a female vet tech protagonist, a one-eyed kitten who she saves and adopts, a male pastor who befriends the vet tech after finding said kitten hiding under his porch, and a pharmaceutical executive antagonist in charge of a dubious feline weight-loss drug.

The two kittens saved by the protagonist also fall in love about 1/4 of the way through the story. One of them has a CNS condition that makes it hard for them to walk, and the point-of-view cat serves as a protector and defender of the disabled one.

Narrative has a lot of focus on the emotional lives of the characters and their relationships, but it is not a romance novel per se. While the title is a Biblical reference and religion and spirituality are important to some of the characters, it is also not meant to support any particular belief system.

Target Market(s)

Cat lovers

Requirements
Must have
• Title: Under Brambled Skies
Author: Delphine Carraway
Tagline (to appear on cover): Even the smallest kitty can change the world
Nice to have
• I originally intended to use the attached photo representing the story's central kittens. I was going to apply some filters to make it look hand-drawn and disguise the low resolution. I quickly realized my graphic design skills are not sufficient to make that look professional, which led me here. If you can make it work with that photo, it would be lovely; if not, I am totally open to alternative concepts.
Should not have
• The appearances and even the ages of the characters are not solidified in the text, in order to allow the reader to imagine them any way they prefer. So I would prefer avoiding any specific visual representations of them, outside of something vague like a silhouette.

```html
<!DOCTYPE html>
<html lang="en">
<head>
<meta charset="utf-8">
<title>Under Brambled Skies — Full Cover</title>
<link rel="stylesheet" href="https://fonts.googleapis.com/css2?family=Courgette&family=Noto+Serif:wght@400&family=Open+Sans:wght@400&display=swap">
<style>
  :root {
    --backdrop: #5f4229;
    --cover-upper: #ece3d2;
    --cover-lower: #d5c8af;
    --back-upper: #f0e7d6;
    --back-lower: #d4c7ae;
    --spine-rule: #8b6a42;
    --title-brown: #7a5a2c;
    --title-glow: #fff6d8;
    --tagline-white: #ffffff;
    --author-ink: #1e1a14;
    --blurb-ink: #2a241b;
    --photo-olive: #8a8458;
    --photo-cream: #efe9df;
    --photo-amber: #d9b98a;
    --placeholder-white: #ffffff;
  }
  * { margin: 0; padding: 0; box-sizing: border-box; }
  html, body { width: 759px; height: 1200px; overflow: hidden; background: var(--backdrop); }

  .cover-wrap {
    position: absolute;
    left: 20px; top: 337px;
    width: 719px; height: 526px;
    overflow: hidden;
  }

  /* Back cover */
  .back-cover {
    position: absolute; left: 0; top: 0;
    width: 342px; height: 526px;
    background: var(--back-upper);
  }
  .back-cover .lower-band {
    position: absolute; left: 0; right: 0; top: 264px; bottom: 0;
    background: var(--back-lower);
  }
  .back-title {
    position: absolute; left: 0; right: 0; top: 52px;
    text-align: center;
    font-family: "Courgette", cursive;
    font-size: 27px; line-height: 30px;
    color: var(--title-brown);
    font-weight: 400;
  }
  .back-title span { display: block; }
  .back-placeholder {
    position: absolute; left: 134px; top: 146px;
    width: 80px; height: 107px;
    background: var(--placeholder-white);
  }
  .back-blurb {
    position: absolute; left: 86px; top: 274px;
    width: 176px;
    font-family: "Noto Serif", serif;
    font-size: 7px; line-height: 8.7px;
    color: var(--blurb-ink);
    text-align: justify;
    hyphens: auto;
  }
  .back-blurb p + p { margin-top: 8.7px; }

  /* Spine */
  .spine {
    position: absolute; left: 342px; top: 0;
    width: 34px; height: 526px;
    background: linear-gradient(to bottom, var(--back-upper) 0 264px, var(--back-lower) 264px 100%);
    border-left: 1px solid var(--spine-rule);
    border-right: 1px solid var(--spine-rule);
  }
  .spine-title, .spine-author {
    position: absolute; left: 50%;
    writing-mode: vertical-rl;
    transform: translateX(-50%);
    white-space: nowrap;
  }
  .spine-title {
    top: 58px;
    font-family: "Courgette", cursive;
    font-size: 17px;
    color: var(--title-brown);
  }
  .spine-author {
    top: 315px;
    font-family: "Open Sans", sans-serif;
    font-size: 12.5px;
    letter-spacing: 2.6px;
    color: var(--author-ink);
  }

  /* Front cover */
  .front-cover {
    position: absolute; left: 376px; top: 0;
    width: 343px; height: 526px;
    overflow: hidden;
    background:
      radial-gradient(ellipse 120px 95px at 172px 150px, rgba(255,255,255,0.95), rgba(255,255,255,0) 70%),
      radial-gradient(ellipse 200px 140px at 90px 50px, rgba(200,188,160,0.35), rgba(0,0,0,0) 70%),
      var(--cover-upper);
  }
  .front-cover .lower-band {
    position: absolute; left: 0; right: 0; top: 264px; bottom: 0;
    background:
      radial-gradient(ellipse 150px 100px at 280px 460px, rgba(190,175,145,0.4), rgba(0,0,0,0) 70%),
      var(--cover-lower);
  }
  .front-title {
    position: absolute; left: 0; right: 0; top: 38px;
    text-align: center;
    font-family: "Courgette", cursive;
    font-size: 41px; line-height: 46px;
    font-weight: 400;
    color: var(--title-brown);
    text-shadow: 0 0 2px var(--title-glow), 0 0 5px var(--title-glow);
  }
  .front-title span { display: block; }
  .kitten-photo {
    position: absolute; left: 60px; top: 156px;
    width: 222px; height: 232px;
  }
  .tagline {
    position: absolute; left: 0; right: 0; top: 397px;
    text-align: center;
    font-family: "Courgette", cursive;
    font-size: 19px; line-height: 24px;
    color: var(--tagline-white);
  }
  .front-author {
    position: absolute; left: 0; right: 0; top: 477px;
    text-align: center;
    font-family: "Open Sans", sans-serif;
    font-size: 15px;
    letter-spacing: 3px;
    color: var(--author-ink);
  }
</style>
</head>
<body>
  <main class="cover-wrap">
    <section class="back-cover">
      <div class="lower-band"></div>
      <h2 class="back-title"><span>Under Brambled</span><span>Skies</span></h2>
      <div class="back-placeholder"></div>
      <div class="back-blurb">
        <p>Lorem ipsum dolor sit amet, consectetur adipiscing elit. Mauris congue orci vitae sapien auctor, et laoreet tellus egestas. Donec suscipit porta dui sed tempor. Class aptent taciti sociosqu ad litora torquent per conubia nostra, per inceptos himenaeos. Fusce non turpis sit amet nunc laoreet pharetra. Integer eu diam in metus posuere malesuada. Maecenas pharetra risus a nulla varius, ac dignissim felis egestas. Curabitur bibendum lectus vel diam facilisis sodales. Morbi velit purus, porta non euismod non, elementum quis justo. Duis non dapibus metus, eu congue tellus. Mauris pulvinar hendrerit orci.</p>
        <p>Sed molestie dui vel mollis pulvinar. Ut ac mi sem. Duis elementum massa metus, ac tempor nisl malesuada sit amet. Fusce auctor feugiat sapien sit amet dignissim. Maecenas sit amet semper neque. Donec sodales, augue vel interdum posuere, justo leo auctor eros, sed vulputate felis felis non ipsum. Cras sit amet consequat mauris. Sed ex metus, rutrum vitae vulputate et, elementum sed sapien.</p>
      </div>
    </section>

    <section class="spine">
      <span class="spine-title">Under Brambled Skies</span>
      <span class="spine-author">Delphine Carraway</span>
    </section>

    <section class="front-cover">
      <div class="lower-band"></div>
      <h1 class="front-title"><span>Under Brambled</span><span>Skies</span></h1>
      <svg class="kitten-photo" viewBox="0 0 500 532" role="img" aria-label="Photograph of two kittens curled together, framed in a rough-edged oval">
        <defs>
          <linearGradient id="photoTone" x1="0" y1="0" x2="0.3" y2="1">
            <stop offset="0" stop-color="#8a8458"/>
            <stop offset="0.45" stop-color="#b7ad8c"/>
            <stop offset="0.75" stop-color="#efe9df"/>
            <stop offset="1" stop-color="#d9b98a"/>
          </linearGradient>
        </defs>
        <path fill="url(#photoTone)" d="M250 4 C330 2 400 30 440 90 C478 150 498 220 494 300 C490 380 460 450 400 495 C350 528 300 532 250 530 C190 530 130 520 80 480 C30 440 6 370 4 290 C2 210 30 140 80 85 C120 40 180 6 250 4 Z"/>
      </svg>
      <p class="tagline">Even the smallest kitty<br>can change the world</p>
      <p class="front-author">Delphine Carraway</p>
    </section>
  </main>
</body>
</html>
```